Milk product packaging

We are ready to begin packaging our product! Exciting! I already have a logo (from Pixel Harbor!) and company name (Tovani Kitchens), but now we need an attractive, attention-drawing and pleasing package design. The product is a healthy flavored milk that needs to appeal to kids from 2 years old and up, moms shopping for kids, and potentially other adults. A hard task, but we don't want to limit the product to kids even though they will be the first customer we will advertise to.

The product will most likely be a flexi cart single serving milk package, like the kind kids take in their lunch boxes, that has a straw attached. It will need to have space for nutritional labeling and space on the back for advertising or things like 'fun facts.'

So far our main logo colors are green, black and white (see the logos attached.) Looking at competitors (Larkfield Organics, Zib Milk, Fenwick Grove) they have used components of farms or cows on their products to appeal to a down-to-earth feel and to promote the idea of a product 'straight from the farm.' This isn't a necessity for me but it was something I noted. There will be multiple flavors of milk, and so far I've been using a bluish purple color for the Radiance blend (which contains blue and purple berries) and a dark yellow for the Breeze blend, an accent to the standard black/white/green color scheme of the logo and materials. So all packages look the same, but a different flavor has a different 'splash' of color to differentiate it. Again, just my thoughts and i'm open to other looks and ideas. We're advertising it as "milk plus a nourishing blend of ....." Statistics say we only have 3-5 seconds to influence the customer to pick up and try our product, so we're looking for a winning design to help us do just that!! We want to lead the way in flavored milk that is healthy, not just added sugar and artificial ingredients. The attached files are the logos we got from Pixel Harbor. Healthy, nourishing, flavored milk!

Reason: Hi! Many designers seem to be busy...just seeing if this helps. So far I love the ideas I'm seeing! Thanks.

```html
<!DOCTYPE html>
<html lang="en">
<head>
<meta charset="utf-8">
<title>Tovani Kitchens – Organic Lowfat Milk</title>
<link rel="stylesheet" href="https://fonts.googleapis.com/css2?family=Fredoka:wght@500&family=Poppins:wght@600;700&family=Lilita+One&display=swap">
<style>
  :root {
    --lime-light: #b2e214;
    --lime-deep: #78c50c;
    --lime-text: #bfe82e;
    --ink: #0e1c28;
    --ink-soft: #2e2e2e;
    --paper: #ffffff;
  }
  * { margin: 0; padding: 0; box-sizing: border-box; }
  html, body { width: 1200px; height: 2942px; overflow: hidden; background: var(--paper); }
  .carton-panel { position: relative; width: 1200px; height: 2942px; overflow: hidden; background: var(--paper); }
  .wave-layer { position: absolute; inset: 0; width: 1200px; height: 2942px; }
  .brand { position: absolute; left: 0; width: 1160px; top: 720px; text-align: center; }
  .brand-dot { display: block; width: 160px; height: 160px; margin: 0 auto 46px; border-radius: 50%; background: var(--lime-deep); }
  .brand-name { font-family: "Fredoka", sans-serif; font-weight: 500; font-size: 74px; color: var(--ink); line-height: 1; }
  .product-copy { position: absolute; left: 0; width: 1124px; top: 1980px; text-align: center; }
  .fat-line { font-family: "Poppins", sans-serif; font-weight: 700; font-size: 64px; color: var(--ink); line-height: 1; }
  .product-name {
    font-family: "Lilita One", sans-serif; font-size: 118px; color: var(--lime-text);
    -webkit-text-stroke: 5px var(--ink); paint-order: stroke fill; letter-spacing: 2px;
    line-height: 1; margin-top: 40px;
  }
  .vitamins { font-family: "Poppins", sans-serif; font-weight: 600; font-size: 62px; letter-spacing: 18px; color: var(--ink); line-height: 1; margin-top: 34px; }
  .volume { position: absolute; right: 82px; top: 2810px; font-family: "Poppins", sans-serif; font-weight: 700; font-size: 68px; color: var(--ink-soft); line-height: 1; }
</style>
</head>
<body>
<main class="carton-panel">
  <svg class="wave-layer" viewBox="0 0 425 1042" preserveAspectRatio="none" aria-hidden="true">
    <defs>
      <linearGradient id="limeWash" x1="0" y1="0" x2="1" y2="1">
        <stop offset="0" stop-color="#b6e414"/>
        <stop offset="1" stop-color="#74c20c"/>
      </linearGradient>
    </defs>
    <path fill="url(#limeWash)" d="M0,0 H425 V190 C395,175 375,80 310,58 C265,44 235,66 205,30 C185,6 150,4 118,22 C70,48 40,150 0,190 Z"/>
    <path fill="url(#limeWash)" d="M0,490 C40,490 72,505 68,545 C64,590 50,630 62,678 C40,676 20,675 0,675 Z"/>
    <path fill="url(#limeWash)" d="M425,700 C390,735 350,800 300,835 C250,870 170,870 140,905 C115,935 90,945 80,1042 H425 Z"/>
  </svg>

  <header class="brand">
    <span class="brand-dot"></span>
    <p class="brand-name">Tovani Kitchens</p>
  </header>

  <section class="product-copy">
    <p class="fat-line">Organic 1 % MilkFat</p>
    <h1 class="product-name">LOWFAT MILK</h1>
    <p class="vitamins">Vitamins A &amp; D</p>
  </section>

  <p class="volume">(236ml)</p>
</main>
</body>
</html>
```